Building and Construction Business Card Design

We need a business card design for a new building and construction company called "Harbourline Estates Pty Ltd" We will build any type of building, but our main focus is luxury homes in Sydney.
We would like our business card to be elegant and strong. We have played around with colours and like greys/black and red, but are open to pretty open minded.
Updates

Project Deadline Extended
Reason: Designs are either plain without any wow, or a little comical. Hopefully we can get some designs that are more eye catching, maybe some bling (silver/ gold script) something different please. Thank you for your submissions so far.

Target Market(s)

high end real estate market

Industry/Entity Type

Construction

Contact Information for Business Card

Teodor Halloran
Director/Fully Licenced Builder
ABN: 72504918337
m: 0491 573 812
e: info@harbourlineestates.com.au
HARBOURLINE ESTATES
website: www.harbourlineestates.com.au

Building and Construction

Colors

Designer to choose colors to be used in the design.

Requirements
Nice to have
• The business name "Harbourline Estates" on one side then all the info on the otherside.

```html
<!DOCTYPE html>
<html lang="en">
<head>
<meta charset="utf-8">
<title>Harbourline Estates – Business Card</title>
<link rel="stylesheet" href="https://fonts.googleapis.com/css2?family=Quicksand:wght@400;500;600&family=Titillium+Web:wght@700&display=swap">
<style>
  :root {
    --backdrop: #2a2828;
    --card: #3b3b3b;
    --card-edge: #333333;
    --band: #f26b6b;
    --band-ink: #3a3a3a;
    --silver-light: #f2f2f2;
    --silver-mid: #c9c9c9;
    --silver-dark: #9a9a9a;
    --icon: #bdbdbd;
  }
  html, body {
    margin: 0;
    width: 1200px;
    height: 1200px;
    overflow: hidden;
    background: var(--backdrop);
  }
  .business-card {
    position: absolute;
    left: 100px;
    top: 294px;
    width: 1000px;
    height: 612px;
    background: var(--card);
    box-shadow: 0 20px 50px rgba(0,0,0,.45);
    overflow: hidden;
  }
  .info-panel {
    position: absolute;
    left: 470px;
    top: 0;
    right: 0;
    bottom: 0;
    background: var(--card);
    box-shadow: -6px 0 12px rgba(0,0,0,.22);
  }
  .silver {
    background: linear-gradient(180deg, var(--silver-light) 0%, var(--silver-mid) 55%, var(--silver-dark) 100%);
    -webkit-background-clip: text;
    background-clip: text;
    color: transparent;
    text-shadow: 0 1px 1px rgba(0,0,0,.25);
  }
  .name-band {
    position: absolute;
    left: 70px;
    top: 190px;
    width: 400px;
    height: 98px;
    background: var(--band);
  }
  .person-name {
    position: absolute;
    right: 26px;
    top: 4px;
    margin: 0;
    font: 700 46px/1.1 "Titillium Web", sans-serif;
    white-space: nowrap;
  }
  .person-title {
    position: absolute;
    right: 26px;
    top: 60px;
    margin: 0;
    font: 500 21px/1.2 "Quicksand", sans-serif;
    color: var(--band-ink);
    white-space: nowrap;
  }
  .company {
    position: absolute;
    left: 0;
    right: 0;
    top: 62px;
    text-align: center;
  }
  .company-name {
    margin: 0;
    font: 600 35px/1.2 "Quicksand", sans-serif;
  }
  .company-abn {
    margin: 8px 0 0;
    font: 600 24px/1.2 "Quicksand", sans-serif;
  }
  .contact-icons {
    position: absolute;
    left: 408px;
    top: 290px;
    width: 26px;
  }
  .contact-icons svg {
    display: block;
    width: 24px;
    height: 24px;
    margin-bottom: 18px;
    fill: none;
    stroke: var(--icon);
    stroke-width: 1.6;
  }
  .contact-list {
    position: absolute;
    left: 40px;
    top: 292px;
    margin: 0;
    padding: 0;
    list-style: none;
    font: 500 25px/42px "Quicksand", sans-serif;
  }
</style>
</head>
<body>
  <article class="business-card">
    <section class="info-panel">
      <div class="company">
        <h2 class="company-name silver">Harbourline Estates Pty Ltd</h2>
        <p class="company-abn silver">ABN&nbsp; 72504918337</p>
      </div>
      <ul class="contact-list">
        <li class="silver">www.harbourlineestates.com.au</li>
        <li class="silver">info@harbourlineestates.com.au</li>
        <li class="silver">0491 573 812</li>
      </ul>
    </section>

    <div class="contact-icons" aria-hidden="true">
      <svg viewBox="0 0 24 24"><circle cx="12" cy="12" r="10"/><ellipse cx="12" cy="12" rx="4.5" ry="10"/><line x1="2" y1="12" x2="22" y2="12"/><path d="M4 7h16M4 17h16"/></svg>
      <svg viewBox="0 0 24 24"><rect x="2" y="5" width="20" height="14"/><path d="M2 5l10 8 10-8"/></svg>
      <svg viewBox="0 0 24 24"><path d="M3 9c0-3 4-5 9-5s9 2 9 5v2h-5V8H8v3H3z"/><rect x="5" y="12" width="14" height="8" rx="1"/><circle cx="12" cy="16" r="2"/></svg>
    </div>

    <div class="name-band">
      <h1 class="person-name silver">Teodor Halloran</h1>
      <p class="person-title">Director/ Fully Licenced Builder</p>
    </div>
  </article>
</body>
</html>
```